Peter Lanford Studios Business Card

Looking for a clear, modern, elegant, sharp business card that conveys a professional yet edgy image to my business as a wedding, portrait, and travel photographer. Would like something that looks vintage yet modern. Need a new business card to grow my business. We are growing the business for Wedding and Event Photography as well as fine art Photography. (Mostly Landscapes)
Updates

I’m looking through designs now but I have a new logo that i want using please.

New logo uploaded please redesign using that

PLEASE ALL DESIGNERS LOOK IN BRIEF FOR NEW LOGO

Target Market(s)

Brides, Grooms, Families with Kids, People looking for Fine Art Photography Artwork

Industry/Entity Type

Photographer

Contact Information for Business Card

Unsure

Font styles to use
Serif

Colors

Designer to choose colors to be used in the design.

Requirements
Must have
• My Website:
• http://lanfordgallery.snapfolio.example
• Phone:
• 555-418-2061
• Email:
• petelanfordgallery@mailbox.example
Nice to have
• Would like a sort of shine on the printing finish.
• I like black I think it looks good on a business card.
• Can try working with my logo (png that I've attached)

```html
<!DOCTYPE html>
<html lang="en">
<head>
<meta charset="utf-8">
<title>Peter Lanford Studios — Business Card</title>
<link rel="stylesheet" href="https://fonts.googleapis.com/css2?family=Questrial&display=swap">
<style>
  :root {
    --backdrop: #d6d6d6;
    --card: #000000;
    --gold: #d9a93f;
    --gold-light: #e8c36a;
    --white: #f2f2f2;
    --glow-strong: rgba(255, 255, 255, 0.42);
    --glow-soft: rgba(255, 255, 255, 0.3);
  }
  * { box-sizing: border-box; margin: 0; padding: 0; }
  html, body {
    width: 1200px; height: 1000px; overflow: hidden;
    background: var(--backdrop);
    font-family: "Questrial", sans-serif;
  }
  .canvas {
    position: relative; width: 1200px; height: 1000px;
    display: flex; flex-direction: column; align-items: center; justify-content: center; gap: 40px;
  }
  .card {
    position: relative; width: 770px; height: 440px;
    background: var(--card);
    box-shadow: 0 6px 18px rgba(0,0,0,0.25);
    overflow: hidden;
  }

  /* Front */
  .sparkle-trail {
    position: absolute; right: 0; top: 0; width: 380px; height: 440px;
    background:
      radial-gradient(ellipse 30% 13% at 66% 20%, var(--glow-strong), transparent),
      radial-gradient(ellipse 20% 16% at 58% 47%, var(--glow-soft), transparent),
      radial-gradient(ellipse 30% 14% at 40% 80%, var(--glow-strong), transparent);
  }
  .brand {
    position: absolute; left: 70px; top: 185px;
  }
  .brand-name {
    color: var(--gold); font-size: 44px; letter-spacing: 0.32em; white-space: nowrap;
  }
  .brand-sub {
    color: var(--gold); font-size: 14px; letter-spacing: 0.55em; text-align: right;
    margin-top: 6px; margin-right: 4px;
  }

  /* Back */
  .services {
    position: absolute; right: 50px; top: 50px; text-align: right; color: var(--gold);
  }
  .services-title { font-size: 30px; letter-spacing: 0.02em; }
  .services-list { font-size: 20px; margin-top: 6px; color: var(--gold-light); }
  .social {
    position: absolute; right: 50px; top: 200px;
    display: flex; align-items: center; gap: 8px;
    color: var(--white); font-size: 19px;
  }
  .social-label { margin-right: 6px; }
  .social-mark {
    width: 20px; height: 20px; border: 2px solid var(--gold); border-radius: 4px;
  }
  .contact {
    position: absolute; left: 50px; bottom: 50px;
    list-style: none; color: var(--white); font-size: 22px;
  }
  .contact-item { display: flex; align-items: center; gap: 16px; height: 36px; }
  .contact-icon { width: 24px; height: 24px; flex: none; }
</style>
</head>
<body>
<main class="canvas">
  <section class="card card-front">
    <div class="sparkle-trail" role="img" aria-label="Trail of white glitter sparkles sweeping up the card"></div>
    <div class="brand">
      <div class="brand-name">PETER LANFORD</div>
      <div class="brand-sub">STUDIOS</div>
    </div>
  </section>

  <section class="card card-back">
    <div class="services">
      <div class="services-title">PHOTOGRAPHY + GALLERIES</div>
      <div class="services-list">Events | Portraits | Fine art</div>
    </div>
    <div class="social">
      <span class="social-label">follow us</span>
      <span class="social-mark"></span>
      <span class="social-mark"></span>
      <span class="social-mark"></span>
    </div>
    <ul class="contact">
      <li class="contact-item">
        <svg class="contact-icon" viewBox="0 0 24 24" fill="none" stroke="var(--gold)" stroke-width="1.8">
          <rect x="7" y="2" width="10" height="20" rx="2"/><line x1="11" y1="18.5" x2="13" y2="18.5"/>
        </svg>
        <span>555 418 2061</span>
      </li>
      <li class="contact-item">
        <svg class="contact-icon" viewBox="0 0 24 24" fill="none" stroke="var(--gold)" stroke-width="1.8">
          <rect x="2" y="5" width="20" height="14" rx="1"/><polyline points="2,5 12,13 22,5"/>
        </svg>
        <span>petelanfordgallery@mailbox.example</span>
      </li>
      <li class="contact-item">
        <svg class="contact-icon" viewBox="0 0 24 24" fill="none" stroke="var(--gold)" stroke-width="1.8">
          <circle cx="12" cy="12" r="10"/><ellipse cx="12" cy="12" rx="4" ry="10"/><line x1="2" y1="12" x2="22" y2="12"/>
        </svg>
        <span>www.lanfordgallery.snapfolio.example</span>
      </li>
    </ul>
  </section>
</main>
</body>
</html>
```